Website design for recruitment solutions

We connect top talents to fast growing employers in Asia. We need to revamp our existing website (currently outdated) and also add more pages to make it more informative for talents and employers.
We need final design output to be for both desktop and mobile devices. The final design output must come with all specifications so it's easier for our dev team to implement. We have a detailed mockup but we expect the design to be significantly changed by the final output. We want the pages to look aesthetic, modern and professional.
Number of Pages Required
5+ page
Requirements
Must have
- - To have Pages design for desktop+mobile. Need to take into account intermediate resolutions like 1365px\1023px\767px\479px, especially if mobile/desktop design differs considerably. Design should be repeatable (between pages), suitable for block-layout.
Nice to have
- In terms of receiving files, we usually work with designers who can deliver files in Figma or Sketch with export to Figma. If in PSD format - please export to Zeplin or Avocode, otherwise will be difficult to open

```html
<!DOCTYPE html>
<html lang="en">
<head>
<meta charset="utf-8">
<title>HIRELANE — Recruitment Solutions</title>
<link href="https://fonts.googleapis.com/css2?family=Montserrat:wght@300;400;500;600;700&family=Poppins:wght@400;500&display=swap" rel="stylesheet">
<style>
:root{
  --blue:#3a6fb0;
  --teal:#12dccb;
  --ink:#6b6b6b;
  --dark:#3a3d45;
  --soft:#f2f2f2;
  --grey:#e8e8e8;
  --field:#cccccc;
  --white:#ffffff;
}
*{margin:0;padding:0;box-sizing:border-box}
html,body{width:1200px;height:5106px;overflow:hidden}
body{position:relative;font-family:"Montserrat",sans-serif;color:var(--ink);background:var(--white)}
.abs{position:absolute}
.photo{position:absolute}

/* hero */
.hero{left:0;top:0;width:1200px;height:800px;background:linear-gradient(110deg,#5a5d60 0%,#7d7a74 40%,#4b4d50 75%,#3a3b3d 100%)}
.nav-line{background:rgba(255,255,255,.45)}
.logo{font-weight:600;color:var(--white);font-size:34px;letter-spacing:1px}
.nav-link{font-size:18px;color:var(--white);letter-spacing:.5px;top:40px}
.nav-link.active{color:var(--teal)}
.account{font-size:18px;color:var(--white);display:flex;align-items:center;gap:8px;left:1000px}
.account.login{color:var(--teal)}
.hero-title{left:117px;top:290px;font-size:86px;font-weight:300;color:var(--white);letter-spacing:2px}
.hero-sub{left:117px;top:405px;font-size:47px;font-weight:300;color:var(--white);line-height:56px;letter-spacing:1px}
.btn-start{left:117px;top:549px;width:389px;height:80px;background:var(--teal);color:var(--white);font-size:44px;font-weight:300;display:flex;align-items:center;justify-content:center;gap:30px;border-radius:3px}
.dot{top:729px;width:36px;height:3px;background:var(--white)}
.dot.on{background:var(--teal)}

/* section headings */
.sec-title{width:1200px;left:0;text-align:center;font-size:90px;font-weight:300;color:var(--blue);letter-spacing:3px}
.sec-lede{width:1200px;left:0;text-align:center;font-size:28px;line-height:34px;font-weight:300;color:var(--ink)}
.crosses{left:520px;width:160px;height:30px}

.card-head{font-size:46px;font-weight:400;color:var(--blue)}
.card-body{font-size:20px;line-height:24px;color:var(--ink);text-align:justify;hyphens:auto}
.btn-more{height:42px;width:130px;background:var(--teal);color:var(--white);font-size:21px;display:flex;align-items:center;justify-content:center;border-radius:4px}

/* signup */
.signup{left:0;top:1751px;width:1200px;height:639px;background:var(--soft)}
.form-title{left:571px;top:1870px;font-size:30px;font-weight:600;color:var(--blue)}
.label{font-size:29px;color:var(--blue);left:565px}
.field{left:565px;width:579px;height:52px;background:var(--field)}
.btn-submit{left:565px;top:2211px;width:579px;height:54px;background:var(--teal);color:#111;font-size:30px;display:flex;align-items:center;justify-content:center}

.how{left:0;top:2390px;width:1200px;height:1055px;background:var(--grey)}

/* testimonial */
.avatar{left:492px;top:3535px;width:216px;height:216px;border-radius:50%;background:radial-gradient(circle at 50% 40%,#b58d6e,#6a6b4e 70%,#4d5342)}
.quote{left:0;width:1200px;top:3806px;text-align:center;font-size:29px;line-height:34px;font-weight:300;color:var(--ink)}
.author{left:0;width:1200px;top:3905px;text-align:center;font-size:27px;font-weight:300;color:var(--ink)}

/* cta */
.cta{left:0;top:4050px;width:1200px;height:330px;background:linear-gradient(90deg,#34373f,#454851 50%,#363940)}
.cta-title{left:43px;top:4140px;font-size:52px;font-weight:700;color:var(--white)}
.cta-text{left:43px;top:4222px;width:680px;font-size:20px;line-height:25px;color:var(--white);text-align:justify}
.btn-join{left:870px;top:4145px;width:215px;height:99px;border:3px solid var(--teal);color:var(--teal);font-size:44px;display:flex;align-items:center;justify-content:center}

/* footer */
.mail-head{left:135px;top:4530px;font-family:"Poppins",sans-serif;font-size:35px;font-weight:500;color:var(--blue)}
.phone{left:900px;width:211px;text-align:right;top:4515px;font-size:21px;color:var(--blue)}
.email{left:900px;width:195px;text-align:right;top:4555px;font-size:12px;color:var(--blue)}
.rule{left:135px;top:4601px;width:976px;height:1px;background:#d8d8d8}
.foot-logo{left:113px;top:4700px;font-size:52px;font-weight:500;color:var(--blue);letter-spacing:1px}
.tagline{left:113px;top:4806px;width:210px;font-size:12px;line-height:15px;color:var(--blue)}
.social{top:4902px;width:36px;height:36px;border:2px solid var(--blue);border-radius:50%}
.col-head{top:4718px;font-family:"Poppins",sans-serif;font-size:18px;font-weight:500;color:var(--blue)}
.col-link{font-size:12px;color:var(--blue)}
.sub-box{left:815px;top:4763px;width:307px;height:48px;border:1.5px solid var(--blue);border-radius:24px;font-size:12px;color:#999;padding-left:20px;display:flex;align-items:center}
.sub-btn{left:997px;top:4765px;width:123px;height:44px;border-radius:22px;background:var(--blue);color:#111;font-size:14px;font-weight:600;display:flex;align-items:center;justify-content:center}
.copyright{left:0;top:5014px;width:1200px;height:92px;background:#e6e6e6;color:var(--blue);font-size:19px;display:flex;align-items:center;justify-content:center}
</style>
</head>
<body>

<!-- hero -->
<div class="abs hero" role="img" aria-label="Photo of a smiling man working at a desk in an office"></div>
<div class="abs nav-line" style="left:0;top:100px;width:1200px;height:1px"></div>
<div class="abs nav-line" style="left:220px;top:0;width:1px;height:100px"></div>
<div class="abs nav-line" style="left:982px;top:0;width:1px;height:100px"></div>
<div class="abs logo" style="left:32px;top:30px">HIRELANE</div>
<div class="abs nav-link active" style="left:262px">HOME</div>
<div class="abs nav-link" style="left:345px">ABOUT US</div>
<div class="abs nav-link" style="left:474px">HOW WE WORK</div>
<div class="abs nav-link" style="left:656px">EMPLOYERS</div>
<div class="abs nav-link" style="left:797px">REGISTRATION</div>
<div class="abs account login" style="top:20px">
  <svg width="26" height="26" viewBox="0 0 26 26" fill="none" stroke="#12dccb" stroke-width="1.6"><circle cx="13" cy="13" r="11.5"/><rect x="8.5" y="12" width="9" height="7" rx="1"/><path d="M10 12V9.5a3 3 0 0 1 6 0V12"/></svg>LOG IN
</div>
<div class="abs account" style="top:54px">
  <svg width="26" height="26" viewBox="0 0 26 26" fill="none" stroke="#fff" stroke-width="1.6"><circle cx="13" cy="13" r="11.5"/><path d="M13 7v12M7 13h12"/></svg>REGISTER
</div>
<svg class="abs" style="left:50px;top:400px" width="26" height="46" viewBox="0 0 26 46" fill="none" stroke="rgba(255,255,255,.6)" stroke-width="2"><path d="M24 2 3 23l21 21"/></svg>
<svg class="abs" style="left:1124px;top:400px" width="26" height="46" viewBox="0 0 26 46" fill="none" stroke="rgba(255,255,255,.6)" stroke-width="2"><path d="M2 2l21 21L2 44"/></svg>
<div class="abs hero-title">LOREM IPSUM</div>
<div class="abs hero-sub">WE CONNECT TOP TALENTS INTO<br>FAST GROWING EMPLOWERS IN ASIA</div>
<div class="abs btn-start">Get Started <span>&gt;</span></div>
<div class="abs dot on" style="left:530px"></div>
<div class="abs dot" style="left:582px"></div>
<div class="abs dot" style="left:635px"></div>

<!-- about -->
<div class="abs sec-title" style="top:866px">ABOUT US</div>
<svg class="abs crosses" style="top:1000px" viewBox="0 0 160 30" stroke="#3a6fb0" stroke-width="2.5"><path d="M8 6l18 18M26 6 8 24M71 6l18 18M89 6 71 24M134 6l18 18M152 6l-18 18"/></svg>
<div class="abs sec-lede" style="top:1054px">Lorem ipsum dolor sit amet, consectetuer adipiscing elit.<br>Aenean commodo ligula eget dolor. Aenean massa. Cum<br>sociis natoque</div>
<div class="photo" style="left:73px;top:1273px;width:502px;height:335px;background:linear-gradient(100deg,#6c5a4d,#b2a08a 45%,#8a6b56 75%,#d7c6ae)" role="img" aria-label="Photo of a team gathered around a table looking at a tablet"></div>
<div class="abs card-head" style="left:619px;top:1266px">Lorem ipsum dolor</div>
<div class="abs card-body" style="left:625px;top:1336px;width:512px">We are a recruitment company, connecting top talents to fast growing companies in Asia .Since inception, our talent pool and business have grown organically.<br>However, we are now in the process of scaling up and we are looking to revamp our public website to encourage talents to join our pool via website registration (instead of sending CVs to our inboxes).</div>
<div class="abs btn-more" style="left:627px;top:1567px">More</div>

<!-- sign up -->
<div class="abs signup"></div>
<div class="photo" style="left:125px;top:1818px;width:335px;height:502px;background:linear-gradient(160deg,#7a4a3a,#5a3a30 40%,#6e5646 70%,#8c3d3a)" role="img" aria-label="Photo of two colleagues reviewing work on a tablet at a wooden table"></div>
<div class="abs form-title">Sign Up For Free!</div>
<div class="abs label" style="top:1950px">Name</div>
<div class="abs field" style="top:1993px"></div>
<div class="abs label" style="top:2070px">Email</div>
<div class="abs field" style="top:2114px"></div>
<div class="abs btn-submit">Start Now</div>

<!-- how we work -->
<div class="abs how"></div>
<svg class="abs" style="left:576px;top:2389px" width="48" height="26" viewBox="0 0 48 26"><path d="M0 0h48L24 25z" fill="#f2f2f2"/></svg>
<div class="abs sec-title" style="top:2520px">HOW WE WORK</div>
<svg class="abs crosses" style="top:2652px" viewBox="0 0 160 30" stroke="#3a6fb0" stroke-width="2.5"><path d="M8 6l18 18M26 6 8 24M71 6l18 18M89 6 71 24M134 6l18 18M152 6l-18 18"/></svg>
<div class="abs sec-lede" style="top:2722px">Lorem ipsum dolor sit amet, consectetuer adipiscing elit.<br>Aenean commodo ligula eget dolor. Aenean massa. Cum<br>sociis natoque</div>
<div class="abs card-head" style="left:52px;top:2918px">Lorem ipsum dolor</div>
<div class="abs card-body" style="left:52px;top:2987px;width:514px">We are a recruitment company, connecting top talents to fast growing companies in Asia .Since inception, our talent pool and business have grown organically.<br>However, we are now in the process of scaling up and we are looking to revamp our public website to encourage talents to join our pool via website registration (instead of sending CVs to our inboxes).</div>
<div class="abs btn-more" style="left:55px;top:3220px">More</div>
<div class="photo" style="left:619px;top:2925px;width:502px;height:333px;background:linear-gradient(100deg,#6c5a4d,#b2a08a 45%,#8a6b56 75%,#d7c6ae)" role="img" aria-label="Photo of a team gathered around a table looking at a tablet"></div>

<!-- testimonial -->
<div class="photo avatar" role="img" aria-label="Portrait photo of the quoted client"></div>
<svg class="abs" style="left:74px;top:3665px" width="22" height="40" viewBox="0 0 22 40" fill="none" stroke="#999" stroke-width="2"><path d="M20 2 2 20l18 18"/></svg>
<svg class="abs" style="left:1104px;top:3665px" width="22" height="40" viewBox="0 0 22 40" fill="none" stroke="#999" stroke-width="2"><path d="M2 2l18 18L2 38"/></svg>
<div class="abs quote">“Lorem ipsum dolor sit amet, consectetuer adipiscing elit.<br>Aenean commodo ligula eget natoque”</div>
<div class="abs author">– Mira Holt</div>

<!-- call to action -->
<div class="abs cta" role="img" aria-label="Darkened photo of a group of people using phones and tablets"></div>
<div class="abs cta-title">Lorem ipsum dolor sit</div>
<div class="abs cta-text">Lorem ipsum dolor sit amet, consectetuer adipiscing elit, sed diam nonummy nibh euismod tincidunt ut laoreet dolore.</div>
<div class="abs btn-join">Join Us</div>

<!-- footer -->
<div class="abs mail-head">Let’s Join Our Team, Mail Us</div>
<div class="abs phone">+00 000 000 000</div>
<div class="abs email">abcdefghij@hirelane.com</div>
<div class="abs rule"></div>
<div class="abs foot-logo">HIRELANE</div>
<div class="abs tagline">We are a data-driven digital marketing agency focusing on growing your business.</div>
<div class="abs social" style="left:113px"></div>
<div class="abs social" style="left:176px"></div>
<div class="abs social" style="left:238px"></div>

<div class="abs col-head" style="left:436px">Services</div>
<div class="abs col-link" style="left:436px;top:4776px">Menu 01</div>
<div class="abs col-link" style="left:436px;top:4816px">Menu 01</div>
<div class="abs col-link" style="left:436px;top:4854px">Menu 01</div>
<div class="abs col-link" style="left:436px;top:4893px">Menu 01</div>
<div class="abs col-link" style="left:436px;top:4933px">Menu 01</div>

<div class="abs col-head" style="left:609px">Useful Links</div>
<div class="abs col-link" style="left:609px;top:4776px">About</div>
<div class="abs col-link" style="left:609px;top:4816px">Blog</div>
<div class="abs col-link" style="left:609px;top:4854px">Contact</div>
<div class="abs col-link" style="left:609px;top:4893px">Appoinment</div>

<div class="abs col-head" style="left:815px;top:4712px">Subscribe</div>
<div class="abs sub-box">Enter your mail</div>
<div class="abs sub-btn">Subscribe</div>

<div class="abs copyright">Copyright ©2020 All rights reserved by Norvale Studio</div>

</body>
</html>
```